WordPress Design for both website and landing page for an expert

I need a clean and stylish design for my new website. I work as an expert (see attached file WHY HOW WHAT), my product is expert opinion (reports) for company evaluations You can use all of the attached pictures colored or black / white. The person is me, you can add other pictures, if you want. The design should be clean and stylish, so you could use white, black, gray, silver and / or one additional color. I have added an idea about my website, see attached file CONCEPT WEBSITE If you have any more information, please do not hesitate to contact us 'Hesitate to ask me ...

```html
<!DOCTYPE html>
<html lang="en">
<head>
<meta charset="utf-8">
<title>Lukas M. Berndt – About</title>
<link rel="stylesheet" href="https://fonts.googleapis.com/css2?family=Montserrat:wght@400;500;600;700&family=Noto+Serif:wght@400&display=swap">
<style>
  :root {
    --ink: #24272c;
    --muted: #8c9096;
    --line: #d5d8dc;
    --pale: #eef1f4;
    --dark: #3a3e44;
    --white: #ffffff;
    --silver-1: #f1f2f3;
    --silver-2: #9ea1a5;
  }
  * { margin: 0; padding: 0; box-sizing: border-box; }
  html, body { width: 1200px; height: 2335px; overflow: hidden; background: var(--white); }
  body { position: relative; font-family: "Noto Serif", Georgia, serif; color: var(--ink); }
  .abs { position: absolute; }
  .sans { font-family: "Montserrat", Arial, sans-serif; }

  /* header */
  .brand { left: 67px; top: 46px; display: flex; align-items: center; gap: 12px; }
  .brand-dot { width: 16px; height: 16px; border-radius: 50%; background: var(--ink); }
  .brand-name { font-family: "Montserrat", Arial, sans-serif; font-size: 17px; letter-spacing: 4px; font-weight: 500; color: var(--ink); }
  .nav { top: 60px; display: flex; font-family: "Montserrat", Arial, sans-serif; font-size: 12px; letter-spacing: 2px; font-weight: 600; }
  .nav a { position: absolute; white-space: nowrap; color: var(--ink); text-decoration: none; }
  .nav a.is-active { color: var(--muted); }

  /* hero */
  .hero { left: 137px; top: 196px; width: 926px; height: 377px;
    background: linear-gradient(90deg, #8e9294 0%, #b9bcbc 30%, #5f6366 42%, #a6a9aa 58%, #d4d6d6 80%, #bfc2c3 100%); }
  .hero-title { left: 137px; width: 926px; top: 345px; text-align: center; color: var(--white);
    font-family: "Montserrat", Arial, sans-serif; font-size: 42px; letter-spacing: 5px; font-weight: 500; }
  .hero-sub { left: 137px; width: 926px; top: 396px; text-align: center; color: var(--white);
    font-family: "Montserrat", Arial, sans-serif; font-size: 15px; }

  /* experience */
  .field-panel { left: 635px; top: 573px; width: 282px; height: 571px; background: var(--pale); }
  .section-title { font-family: "Montserrat", Arial, sans-serif; font-weight: 500; font-size: 27px; text-align: center; width: 1200px; left: 0; }
  .rule { width: 69px; height: 1px; background: var(--line); top: 690px; }
  .exp-label { font-family: "Montserrat", Arial, sans-serif; font-size: 15px; font-weight: 700; letter-spacing: 3px; line-height: 26px; }
  .exp-text { font-size: 14px; line-height: 26px; color: var(--muted); }
  .activity { left: 669px; display: flex; }
  .activity svg { position: absolute; left: 0; top: -8px; }
  .activity p { position: relative; font-size: 14px; line-height: 26px; color: var(--muted); }

  /* education */
  .edu-band { left: 0; top: 1144px; width: 1200px; height: 472px; background: var(--dark); }
  .edu-title { color: var(--white); top: 1207px; }
  .edu-label { width: 200px; text-align: center; font-size: 14px; line-height: 25px; color: var(--white); }
  .pin-year { font-family: "Montserrat", Arial, sans-serif; font-weight: 700; font-size: 16px; }

  /* partners */
  .partner-badge { background: var(--pale); }

  /* call to action */
  .cta { left: 0; top: 1988px; width: 1200px; height: 277px; background: var(--pale); }
  .cta-text { left: 0; width: 1200px; top: 2047px; text-align: center; font-family: "Montserrat", Arial, sans-serif; font-size: 26px; line-height: 39px; font-weight: 500; }
  .cta-button { left: 493px; top: 2157px; width: 214px; height: 40px; border: 1px solid #9a9ea3; border-radius: 20px;
    display: flex; align-items: center; justify-content: center; font-family: "Montserrat", Arial, sans-serif;
    font-size: 12px; font-weight: 600; letter-spacing: 1.5px; color: var(--ink); }

  /* footer */
  .footer { left: 0; top: 2265px; width: 1200px; height: 70px; background: var(--dark); }
  .footer-copy { left: 137px; top: 2293px; font-family: "Montserrat", Arial, sans-serif; font-size: 11px; color: #a7abb0; }
  .footer-links { left: 840px; top: 2293px; font-family: "Montserrat", Arial, sans-serif; font-size: 11px; color: #a7abb0; word-spacing: 3px; }
  .to-top { left: 1111px; top: 2280px; width: 40px; height: 40px; border-radius: 50%; background: #7d8186; }
</style>
</head>
<body>

  <header>
    <div class="abs brand"><span class="brand-dot"></span><span class="brand-name">LUKAS BERNDT</span></div>
    <nav class="abs nav">
      <a style="left:593px">HOME</a>
      <a class="is-active" style="left:674px">ABOUT</a>
      <a style="left:763px">WHAT I DO</a>
      <a style="left:886px">WHY / HOW I DO</a>
      <a style="left:1055px">CONTACT</a>
    </nav>
  </header>

  <section>
    <div class="abs hero" role="img" aria-label="Portrait photo of the expert in a suit standing in a bright modern corridor"></div>
    <h1 class="abs hero-title">LUKAS M. BERNDT</h1>
    <p class="abs hero-sub">Expert for company valuations</p>
  </section>

  <section>
    <div class="abs field-panel"></div>
    <h2 class="abs section-title" style="top:628px">Professional experience</h2>
    <div class="abs rule" style="left:283px"></div>
    <div class="abs rule" style="left:669px"></div>

    <div class="abs" style="left:283px;top:718px">
      <h3 class="exp-label">10 YEARS</h3>
      <p class="exp-text">Managing dircetor in the<br>fitness market</p>
    </div>
    <div class="abs" style="left:283px;top:821px">
      <h3 class="exp-label">10 YEARS</h3>
      <p class="exp-text">CMO / business trainer / CEO in an<br>german industrial company<br>(fitness industry)</p>
    </div>
    <div class="abs" style="left:283px;top:950px">
      <h3 class="exp-label">HSPW</h3>
      <p class="exp-text">Outside lecturer</p>
    </div>
    <div class="abs" style="left:283px;top:1027px">
      <h3 class="exp-label">HSPW</h3>
      <p class="exp-text">Expert</p>
    </div>

    <h3 class="abs exp-label" style="left:669px;top:718px">FIELD<br>OF ACTIVITY</h3>
    <div class="abs activity" style="top:797px">
      <svg width="36" height="36" viewBox="0 0 36 36"><circle cx="18" cy="18" r="16" fill="none" stroke="#fff" stroke-width="1.5"/><path d="M10 19l6 6 11-13" fill="none" stroke="#fff" stroke-width="1.5"/></svg>
      <p>Appraisals Company Valuation<br>Marketing</p>
    </div>
    <div class="abs activity" style="top:874px">
      <svg width="36" height="36" viewBox="0 0 36 36"><circle cx="18" cy="18" r="16" fill="none" stroke="#fff" stroke-width="1.5"/><path d="M10 19l6 6 11-13" fill="none" stroke="#fff" stroke-width="1.5"/></svg>
      <p>Strategic Corporate<br>Governance</p>
    </div>
    <div class="abs activity" style="top:952px">
      <svg width="36" height="36" viewBox="0 0 36 36"><circle cx="18" cy="18" r="16" fill="none" stroke="#fff" stroke-width="1.5"/><path d="M10 19l6 6 11-13" fill="none" stroke="#fff" stroke-width="1.5"/></svg>
      <p>Corporate Health Management</p>
    </div>
    <div class="abs activity" style="top:1003px">
      <svg width="36" height="36" viewBox="0 0 36 36"><circle cx="18" cy="18" r="16" fill="none" stroke="#fff" stroke-width="1.5"/><path d="M10 19l6 6 11-13" fill="none" stroke="#fff" stroke-width="1.5"/></svg>
      <p>Change Management</p>
    </div>
  </section>

  <section>
    <div class="abs edu-band"></div>
    <h2 class="abs section-title edu-title">Educations</h2>

    <p class="abs edu-label" style="left:277px;top:1270px">staat. Geprüfter Be-<br>triebswirt (BA)</p>
    <p class="abs edu-label" style="left:722px;top:1270px">Business Trainer<br>BVTA</p>
    <p class="abs edu-label" style="left:499px;top:1503px">Dipl.-Kfm.<br>(FH)</p>

    <svg class="abs" style="left:0;top:1300px" width="1200" height="210" viewBox="0 1300 1200 210">
      <defs>
        <linearGradient id="silver" x1="0" y1="0" x2="1" y2="1">
          <stop offset="0" stop-color="#f4f5f6"/>
          <stop offset="1" stop-color="#8f9296"/>
        </linearGradient>
        <radialGradient id="inner-dark" cx="0.4" cy="0.35" r="0.7">
          <stop offset="0" stop-color="#9a9da1"/>
          <stop offset="1" stop-color="#55595e"/>
        </radialGradient>
      </defs>
      <!-- pin 2000, point up -->
      <path d="M377 1335 Q392 1364 425 1380 A64 64 0 1 1 329 1380 Q362 1364 377 1335Z" fill="url(#silver)"/>
      <circle cx="377" cy="1424" r="44" fill="#fff"/>
      <!-- pin 2005, point down -->
      <path d="M599 1487 Q584 1458 551 1442 A64 64 0 1 1 647 1442 Q614 1458 599 1487Z" fill="url(#silver)"/>
      <circle cx="599" cy="1398" r="44" fill="url(#inner-dark)"/>
      <!-- pin 2010, point up -->
      <path d="M822 1335 Q837 1364 870 1380 A64 64 0 1 1 774 1380 Q807 1364 822 1335Z" fill="url(#silver)"/>
      <circle cx="822" cy="1424" r="44" fill="#fff"/>
      <!-- arrows -->
      <g fill="none" stroke="#9ea2a7" stroke-width="1.3">
        <path d="M481 1410h16M492 1405l5 5-5 5"/>
        <path d="M703 1410h16M714 1405l5 5-5 5"/>
        <path d="M251 1403l-6 7 6 7"/>
        <path d="M948 1403l6 7-6 7"/>
      </g>
      <text class="pin-year" x="377" y="1430" text-anchor="middle" fill="#24272c">2000</text>
      <text class="pin-year" x="599" y="1404" text-anchor="middle" fill="#fff">2005</text>
      <text class="pin-year" x="822" y="1430" text-anchor="middle" fill="#24272c">2010</text>
    </svg>
  </section>

  <section>
    <h2 class="abs section-title" style="top:1680px">Partners</h2>
    <div class="abs partner-badge" role="img" aria-label="Partner badge" style="left:350px;top:1767px;width:218px;height:109px"></div>
    <div class="abs partner-badge" role="img" aria-label="Partner badge" style="left:634px;top:1800px;width:216px;height:54px;border-radius:27px"></div>
  </section>

  <section>
    <div class="abs cta"></div>
    <p class="abs cta-text">You need an opinion to determine<br>the value of your company</p>
    <a class="abs cta-button">CONTACT NOW!</a>
  </section>

  <footer>
    <div class="abs footer"></div>
    <p class="abs footer-copy">© 2018 Lukas M. Berndt. All Rights Reserved</p>
    <p class="abs footer-links">Data protection &nbsp;|&nbsp; Cookies &nbsp;|&nbsp; imprint</p>
    <svg class="abs to-top" viewBox="0 0 40 40"><path d="M20 26V14M15 19l5-5 5 5" fill="none" stroke="#fff" stroke-width="1.3"/></svg>
  </footer>

</body>
</html>
```